Re-brand our business and design!

We need a simple informational website (editable for in the future use)
We need our logo(we have included logo), name, who we are, and what we do displayed.

This is our current site (which is not acceptable, and only a template site): all our information is on this site, please use it forreferanceofinformation.
Www.brightlanefixers.com

Target Market(s)

Real estate brokers, and realtors,homeowners, and anyone looking for home repairs.

Industry/Entity Type

Business

Number of Pages Required

4 page

Font styles to use
Sans Serif

Requirements
Must have
• Our name, contact info, services, and our logo (which we will Email upon request)
• MUST have originality to the site.
• custom "contact us form" or request an estimate form.
Nice to have
• page for real customer testimonies.
• page for our previous work where we can upload pics of completed jobs.
Should not have
• any infringements on any copyrights or plagiarism at all.

```html
<!DOCTYPE html>
<html lang="en">
<head>
<meta charset="utf-8">
<title>Bright Lane Fixers</title>
<link href="https://fonts.googleapis.com/css2?family=Open+Sans:wght@400;600&display=swap" rel="stylesheet">
<style>
:root{
  --red:#e30d0d;
  --ink:#333;
  --muted:#555;
  --grey-band:#e1e1e1;
  --footer:#e7e7e7;
  --line:#d6d6d6;
  --white:#fff;
}
*{margin:0;padding:0;box-sizing:border-box}
html,body{width:1022px;height:1200px;overflow:hidden;background:var(--white)}
body{position:relative;font-family:"Open Sans",Arial,sans-serif;color:var(--ink)}
.abs{position:absolute}

/* header */
.site-header{left:0;top:0;width:1022px;height:57px;background:var(--white)}
.brand{left:192px;top:0;width:144px;height:64px;background:var(--white);box-shadow:0 1px 4px rgba(0,0,0,.25);z-index:3;display:flex;flex-direction:column;align-items:center;justify-content:center;gap:2px}
.brand-mark{display:flex;align-items:center;gap:5px}
.brand-mark i{width:10px;height:10px;background:var(--red);display:block}
.brand-name{font-weight:600;font-size:11px;color:#111}
.brand-sub{font-weight:600;font-size:7px;color:#777}
.top-contact{right:192px;top:8px;font-size:9px;color:#555;display:flex;align-items:center;gap:6px}
.top-contact .sep{color:#ccc}
.main-nav{right:192px;top:32px;display:flex;gap:23px;font-size:10.5px}
.main-nav a{color:#444;text-decoration:none;position:relative}
.main-nav a.active::after{content:"";position:absolute;left:0;right:0;top:21px;height:3px;background:var(--red)}

/* hero */
.hero{left:0;top:57px;width:1022px;height:319px;background:linear-gradient(180deg,#9a8a80 0%,#b59c8c 35%,#8c7a70 65%,#4f6b3c 100%);border-bottom:3px solid var(--red)}
.hero-panel{left:314px;top:131px;width:420px;height:196px;background:rgba(40,30,25,.35)}
.hero-title{left:443px;top:145px;font-size:27px;color:var(--white);font-weight:400}
.hero-text{left:443px;top:183px;width:265px;font-size:9.5px;line-height:14px;color:var(--white)}
.btn{background:var(--red);color:var(--white);font-size:9.5px;display:flex;align-items:center;justify-content:center;text-decoration:none}
.hero-btn{left:442px;top:270px;width:76px;height:21px;font-size:10.5px}
.dots{display:flex;gap:5px}
.dots span{width:7px;height:7px;border-radius:50%;background:#ddd;display:block}
.dots span.on{background:var(--red)}
.hero-dots{left:490px;top:354px}

/* services */
.service{width:200px;text-align:center}
.service-icon{width:100px;height:100px;border:1px solid #bbb;border-radius:50%;margin:0 auto;display:flex;align-items:center;justify-content:center}
.service h3{font-weight:400;font-size:21px;color:var(--red);margin-top:19px}
.service p{font-size:8px;line-height:11.5px;color:var(--muted);margin-top:9px}
.svc-dots{left:502px;top:643px}
.svc-dots span{width:6px;height:6px}

/* welcome */
.welcome{left:0;top:670px;width:1022px;height:284px;background:var(--grey-band)}
.welcome h2{left:212px;top:24px;font-weight:400;font-size:21px;color:#555}
.welcome h2 b{font-weight:400;color:#222}
.welcome .copy{left:214px;top:66px;width:402px;font-size:7.9px;line-height:11.5px;color:#333}
.welcome .copy p+p{margin-top:11.5px}
.welcome-btn{left:214px;top:223px;width:71px;height:24px}
.photo-frame{left:644px;top:32px;width:186px;height:215px;background:var(--white);border:1px solid #c8c8c8;padding:6px}
.photo-frame div{width:100%;height:100%;background:linear-gradient(135deg,#c9a66b,#8a7a6a 55%,#e4d2cf)}

/* projects */
.projects-title{left:0;top:978px;width:1022px;text-align:center;font-size:21px;font-weight:400;color:#555}
.projects-title b{font-weight:400;color:#222}
.thumbs{left:192px;top:1034px;width:638px;display:flex;justify-content:space-between}
.thumbs div{width:97px;height:74px}

/* footer */
.site-footer{left:0;top:1130px;width:1022px;height:70px;background:var(--footer)}
.foot-nav{left:193px;top:13px;display:flex;gap:23px;font-size:10.5px}
.foot-nav a{color:#555;text-decoration:none}
.foot-nav a.active{color:var(--red)}
.copyright{left:192px;top:39px;font-size:7px;color:#333}
.copyright span{color:var(--red)}
.social{right:192px;top:16px;display:flex;gap:5px}
.social span{width:14px;height:14px;border-radius:50%;background:#8a8a8a;display:block}
.foot-contact{right:192px;top:41px;font-size:11.5px;color:#555}
.foot-contact .sep{color:#bbb;margin:0 5px}
</style>
</head>
<body>

<header class="site-header abs">
  <div class="brand abs">
    <div class="brand-mark"><i></i><span class="brand-name">Bright Lane Fixers</span></div>
    <span class="brand-sub">And Maintenance</span>
  </div>
  <div class="top-contact abs">
    <svg width="11" height="8" viewBox="0 0 11 8"><rect width="11" height="8" fill="#222"/><path d="M0 0 L5.5 4.5 L11 0" stroke="#fff" fill="none" stroke-width="1"/></svg>
    <span>Dana@brightlanefixers.com</span>
    <span class="sep">|</span>
    <svg width="9" height="11" viewBox="0 0 9 11"><path d="M2 0 L4 3 L3 4.5 Q4 7 6 8 L7.5 7 L9 9.5 L7.5 11 Q1 9 0 1.5 Z" fill="#222"/></svg>
    <span>812-555-0147</span>
  </div>
  <nav class="main-nav abs">
    <a class="active" href="#">Home</a><a href="#">Services</a><a href="#">About</a><a href="#">Projects</a><a href="#">Contact</a>
  </nav>
</header>

<section class="hero abs" role="img" aria-label="Photo of a brick family house with a smiling repairman in a hard hat giving a thumbs up"></section>
<div class="hero-panel abs"></div>
<h1 class="hero-title abs">We Build Your Dream</h1>
<p class="hero-text abs">Looking for someone to help get your listing ready to show? A complete Home Repair Solution? Did an inspection reveal repairs needed before closing? Bright Lane Fixers can help!</p>
<a class="btn hero-btn abs" href="#">Learn More</a>
<div class="dots hero-dots abs"><span></span><span class="on"></span><span></span><span></span></div>

<div class="service abs" style="left:194px;top:412px">
  <div class="service-icon">
    <svg width="44" height="44" viewBox="0 0 44 44"><g transform="rotate(-45 22 22)" fill="#777"><rect x="6" y="17" width="26" height="9"/><rect x="32" y="18" width="9" height="7" rx="1"/><path d="M6 26 L8 29 L10 26 L12 29 L14 26 L16 29 L18 26 L20 29 L22 26 L24 29 L26 26 L28 29 L30 26 L32 26 Z"/></g></svg>
  </div>
  <h3>Carpentry</h3>
  <p>Stairs, Floors, Decks, Fences<br>Storage sheds, Storage shelving and doors<br>Vapor barrier repair/installation, Attic and crawl space</p>
</div>
<div class="service abs" style="left:410px;top:412px">
  <div class="service-icon">
    <svg width="40" height="46" viewBox="0 0 40 46"><g fill="#777"><rect x="16" y="2" width="10" height="3"/><rect x="19" y="5" width="4" height="5"/><rect x="2" y="12" width="12" height="8"/><rect x="12" y="10" width="18" height="12" rx="3"/><rect x="26" y="18" width="7" height="10"/><path d="M29.5 33 Q26 39 29.5 41 Q33 39 29.5 33Z"/></g></svg>
  </div>
  <h3>Plumbing</h3>
  <p>Bathrooms, Kitchens, Washer/Dryer Hook Up<br>Clogged drains, Toilets, Tubs/Showers<br>Sinks, Garbage disposals, Leaking faucets</p>
</div>
<div class="service abs" style="left:628px;top:412px">
  <div class="service-icon">
    <svg width="48" height="44" viewBox="0 0 48 44"><g fill="none" stroke="#777" stroke-width="2"><rect x="13" y="6" width="22" height="32" fill="#777"/><path d="M13 6 L2 2 L2 42 L13 38"/><path d="M35 6 L46 2 L46 42 L35 38"/><path d="M7 4 L7 40 M41 4 L41 40 M2 22 L13 22 M35 22 L46 22"/></g></svg>
  </div>
  <h3>Doors &amp; Windows</h3>
  <p>Weatherstripping, Replacements<br>Glass and Screen Installation and Repair, Install locksets</p>
</div>
<div class="dots svc-dots abs"><span class="on"></span><span></span></div>

<section class="welcome abs">
  <h2 class="abs">Welcome to <b>Bright Lane Fixers</b></h2>
  <div class="copy abs">
    <p>There are many variations of passages of Lorem Ipsum available, but the majority have suffered alteration in some form, by injected humour, or randomised words which don't look even slightly believable. If you are going to use a passage of Lorem Ipsum, you need to be sure there isn't anything embarrassing hidden in the middle of text. All the Lorem Ipsum generators on the Internet tend to repeat predefined chunks as necessary, making this the first true generator on the Internet. It uses a dictionary of over 200 Latin words, combined with a handful of model sentence structures, to generate Lorem Ipsum which looks reasonable. The generated Lorem Ipsum is therefore always free from repetition, injected humour, or non-characteristic words etc.</p>
    <p>There are many variations of passages of Lorem Ipsum available, but the majority have suffered alteration in some form, by injected humour, or randomised words which don't look even slightly believable. If you are going to use a passage of Lorem Ipsum, you need to be sure there isn't anything embarrassing hidden in the middle of text. All the Lorem Ipsum generators on making this the first true generator on the Internet.</p>
  </div>
  <a class="btn welcome-btn abs" href="#">View Services</a>
  <div class="photo-frame abs"><div role="img" aria-label="Photo of a couple reviewing house blueprints outside a building"></div></div>
</section>

<h2 class="projects-title abs">Our <b>Projects</b></h2>
<div class="thumbs abs">
  <div role="img" aria-label="Project photo: two-storey house with lawn" style="background:linear-gradient(180deg,#cfd9e0,#6f7d6a 50%,#4f7a30)"></div>
  <div role="img" aria-label="Project photo: brick homes along a street" style="background:linear-gradient(180deg,#3a78c8,#a37e5a 55%,#3c3a38)"></div>
  <div role="img" aria-label="Project photo: stucco house with orange roof" style="background:linear-gradient(180deg,#cfe3f2,#d98a4a 45%,#5b8a2e)"></div>
  <div role="img" aria-label="Project photo: tudor style cottage with garden" style="background:linear-gradient(180deg,#e9eef0,#8a5a45 45%,#3f6b2c)"></div>
  <div role="img" aria-label="Project photo: new window opening onto sky" style="background:linear-gradient(180deg,#e8e8e8,#8fbce0 50%,#d9d9d9)"></div>
  <div role="img" aria-label="Project photo: renovated living room" style="background:linear-gradient(135deg,#e9e1c8,#c9b27a 60%,#8a7a58)"></div>
</div>

<footer class="site-footer abs">
  <nav class="foot-nav abs">
    <a class="active" href="#">Home</a><a href="#">Services</a><a href="#">About</a><a href="#">Projects</a><a href="#">Contact</a>
  </nav>
  <p class="copyright abs">Copyright © 2016. <span>Bright Lane Fixers And Maintenance LLC.</span> &nbsp;|&nbsp; All rights reserved.</p>
  <div class="social abs" aria-label="Social links"><span></span><span></span><span></span><span></span></div>
  <p class="foot-contact abs">812-555-0147<span class="sep">|</span>Dana@brightlanefixers.com</p>
</footer>

</body>
</html>
```